Business Card and Stationary for Construction/Home Improvement Company
Use Text Compatible with Logo
Business Card and Stationary for Construction/Home Improvement Company - Construction
Professional
Dorian Fensley
Owner
5127 Oakmere Lane Ridgeholt, MS 70194
dorian@tamberlybuild.com
tamberlybuild.com
We Specialize In: Roofing - Asphalt Shingles, Metal Standing Seam, TPO Flat Roofs Patio Covers - Flat Pan, Insulated, Screened Enclosures Gutters - Seamless Aluminum - Custom Steel Commercial - Half Round Siding - Vinyl, Quenlo Board, Vinyl Soffit Storm Shutters - Colonial, Board & Batten, Louvered, Raised Panel Waterproofing - Balconies, Raised Decks, Garage Floors
tamberly tamberly
Designers, I eliminated the designs in black and white because of the Ai file being wrong. Sorry for the mix up.
Designers, The file that I uploaded was an Ai logo file fo use in the designs. The colors are not black, they are a graphite and deep purple/blue. Please let me know if you need a different file to use. Thanks

```html
<!DOCTYPE html>
<html lang="en">
<head>
<meta charset="utf-8">
<title>Tamberly Construction Services – Stationery Concepts</title>
<link rel="stylesheet" href="https://fonts.googleapis.com/css2?family=Montserrat:wght@400;600;700&family=Libre+Baskerville&family=Great+Vibes&display=swap">
<style>
:root{
  --stage:#3b3b3d;
  --navy:#1f1d57;
  --navy-deep:#24226a;
  --paper:#f5f5f6;
  --flap:#e9e9ec;
  --rule:#c9c9cf;
  --field:#ececef;
  --ink:#4a4a52;
  --muted:#8d8d96;
  --label:#d8d8dc;
  --graphite:#5d5d63;
  --photo:#5b5b60;
}
*{box-sizing:border-box;margin:0;padding:0}
html,body{width:1200px;height:254px;overflow:hidden;background:var(--stage);font-family:"Montserrat",sans-serif;color:var(--ink)}
.canvas{position:relative;width:1200px;height:254px}
.piece{position:absolute;background:var(--paper);overflow:hidden}
.navy{background:var(--navy);color:#fff}
.label{position:absolute;font-family:"Libre Baskerville",serif;font-size:2.4px;color:var(--label);text-align:center}
.brand{font-weight:700;color:var(--navy);letter-spacing:.04em;line-height:1}
.navy .brand,.brand.on-dark{color:#fff}
.brand small{display:block;font-size:42%;font-weight:700;letter-spacing:.06em;margin-top:.3em}
.tiny{font-size:2px;line-height:1.35}
.micro{font-size:1.6px;line-height:1.35}
.abs{position:absolute}
.script{font-family:"Great Vibes",cursive;color:var(--ink)}
.signature{position:absolute;background:linear-gradient(90deg,#cfcfd6,#e6e6ea);border-radius:2px}
.intro{position:absolute;left:8px;top:60px;width:98px;text-align:center}
.intro .brand{font-size:11px;color:#fff}
.intro p{font-family:"Libre Baskerville",serif;font-size:3.6px;color:var(--label);margin-top:5px}
.field{display:flex;gap:2px;font-size:1.8px;margin-bottom:1.3px}
.field span{flex:1;border-bottom:.3px solid var(--rule);background:var(--field);height:3px}
.slide{position:absolute;width:88px;height:70px;background:var(--paper);padding:5px}
.slide h3{font-size:4px;color:var(--navy);font-weight:700}
.slide h4{font-size:2px;color:var(--muted);font-weight:400;margin-bottom:3px}
.photo{height:16px;background:var(--photo);color:#ccc;font-size:2px;display:flex;align-items:center;justify-content:center}
.disc{position:absolute;border-radius:50%;display:flex;align-items:center;justify-content:center;flex-direction:column}
.hub{width:26%;height:26%;border-radius:50%;background:#fff;border:1.5px solid #ddd}
</style>
</head>
<body>
<main class="canvas">

  <section class="intro">
    <div class="brand">TAMBERLY<small>CONSTRUCTION SERVICES, LLC</small></div>
    <p>Stationary Concepts</p>
  </section>

  <!-- Business card front -->
  <article class="piece card-front" style="left:7px;top:91px;width:47px;height:27px;">
    <div class="brand abs" style="left:3px;top:4px;font-size:4.5px">TAMBERLY<small>CONSTRUCTION SERVICES, LLC</small></div>
    <div class="abs tiny" style="right:3px;top:4px;text-align:right;color:var(--navy)"><b>DORIAN FENSLEY</b><br>Owner</div>
    <div class="abs micro" style="left:3px;top:13px">5127 Oakmere Lane<br>Ridgeholt, MS 70194<br>(504) 555-0147<br>dorian@tamberlybuild.com<br>tamberlybuild.com</div>
    <div class="abs" style="right:0;bottom:0;width:18px;height:5px;background:var(--navy)"></div>
  </article>
  <div class="label" style="left:7px;top:119px;width:47px">Front Card</div>

  <!-- Business card back -->
  <article class="piece navy card-back" style="left:58px;top:91px;width:47px;height:27px;padding:2px 3px">
    <div class="micro" style="text-align:right;font-weight:700;font-size:1.9px">We Specialize In:</div>
    <div class="micro" style="font-size:1.3px;margin-top:1px">
      Roofing - Asphalt Shingles, Metal Standing Seam, TPO Flat Roofs<br>
      Patio Covers - Flat Pan, Insulated, Screened Enclosures<br>
      Gutters - Seamless Aluminum - Custom Steel Commercial - Half Round<br>
      Siding - Vinyl, Quenlo Board, Vinyl Soffit<br>
      Storm Shutters - Colonial, Board &amp; Batten, Louvered, Raised Panel<br>
      Waterproofing - Balconies, Raised Decks, Garage Floors
    </div>
    <div class="brand abs" style="left:3px;bottom:2px;font-size:3.5px">TAMBERLY</div>
  </article>
  <div class="label" style="left:58px;top:119px;width:47px">Back Card Option_01</div>

  <!-- Letterheads -->
  <article class="piece letterhead" style="left:109px;top:15px;width:79px;height:102px;padding:5px">
    <div class="brand" style="font-size:5px">TAMBERLY<small>CONSTRUCTION SERVICES, LLC</small></div>
    <div class="abs micro" style="left:53px;top:5px">5127 Oakmere Lane<br>Ridgeholt, MS 70194<br>(504) 555-0147<br>dorian@tamberlybuild.com</div>
    <div class="micro" style="margin-top:9px">Date<br><br><b>Recipient Name</b><br>Company Name<br>Street Address<br>City, State, Zip</div>
    <p class="micro" style="margin-top:4px">Dear Client, thank you for choosing our crew for your roofing project. We value quality work, honest pricing and clear schedules on every job we take. Our team will contact you soon to confirm details and answer any questions about materials, timing and warranty coverage for your home.</p>
    <p class="micro" style="margin-top:2px">Please keep this letter with your records. If anything changes before work begins, call our office and we will gladly adjust the plan to suit your needs.</p>
    <div class="micro" style="margin-top:3px">Sincerely,</div>
    <div class="signature" role="img" aria-label="Handwritten signature" style="left:5px;top:86px;width:18px;height:5px"></div>
    <div class="abs micro" style="left:5px;top:92px">Dorian Fensley<br>Owner</div>
    <div class="abs micro" style="left:0;right:0;bottom:2px;text-align:center;color:var(--muted)">tamberlybuild.com</div>
  </article>
  <div class="label" style="left:109px;top:118px;width:79px">Letterhead option_01</div>

  <article class="piece letterhead" style="left:193px;top:15px;width:79px;height:102px;padding:5px">
    <div class="brand" style="font-size:5px;text-align:center">TAMBERLY<small>CONSTRUCTION SERVICES, LLC</small></div>
    <div class="micro" style="margin-top:9px">Date<br><br><b>Recipient Name</b><br>Company Name<br>Street Address<br>City, State, Zip</div>
    <p class="micro" style="margin-top:4px">Dear Client, thank you for choosing our crew for your roofing project. We value quality work, honest pricing and clear schedules on every job we take. Our team will contact you soon to confirm details and answer any questions about materials, timing and warranty coverage for your home.</p>
    <p class="micro" style="margin-top:2px">Please keep this letter with your records. If anything changes before work begins, call our office and we will gladly adjust the plan to suit your needs.</p>
    <div class="micro" style="margin-top:3px">Sincerely,</div>
    <div class="signature" role="img" aria-label="Handwritten signature" style="left:5px;top:86px;width:18px;height:5px"></div>
    <div class="abs micro" style="left:5px;top:92px">Dorian Fensley<br>Owner</div>
    <div class="abs micro" style="left:0;right:0;bottom:2px;text-align:center;color:var(--muted)">5127 Oakmere Lane, Ridgeholt, MS 70194 · (504) 555-0147 · tamberlybuild.com</div>
  </article>
  <div class="label" style="left:193px;top:118px;width:79px">Letterhead option_02</div>

  <!-- Email signature -->
  <article class="piece email-signature" style="left:293px;top:43px;width:58px;height:26px">
    <div class="brand abs" style="left:3px;top:4px;font-size:4.5px">TAMBERLY<small>CONSTRUCTION SERVICES, LLC</small></div>
    <div class="abs tiny" style="right:3px;top:4px;text-align:right;color:var(--navy)"><b>DORIAN FENSLEY</b><br>Owner</div>
    <div class="abs micro" style="left:3px;top:13px">5127 Oakmere Lane<br>Ridgeholt, MS 70194<br>(504) 555-0147<br>dorian@tamberlybuild.com</div>
    <div class="abs" style="right:0;bottom:0;width:22px;height:4px;background:var(--navy)"></div>
  </article>
  <div class="label" style="left:293px;top:70px;width:58px">Email Signature</div>

  <!-- Envelopes -->
  <article class="piece envelope-front" style="left:276px;top:80px;width:84px;height:37px">
    <div class="brand abs" style="left:3px;top:4px;font-size:4.5px">TAMBERLY<small>CONSTRUCTION SERVICES, LLC</small></div>
    <div class="abs micro" style="left:3px;top:12px">5127 Oakmere Lane<br>Ridgeholt, MS 70194</div>
  </article>
  <div class="label" style="left:276px;top:118px;width:84px">Envelope_Front</div>

  <article class="piece envelope-back" style="left:364px;top:40px;width:85px;height:77px;background:var(--flap)">
    <svg class="abs" style="left:0;top:0" width="85" height="40" viewBox="0 0 85 40"><path d="M0 0H85V14L42.5 30L0 14Z" fill="var(--navy)"/></svg>
    <div class="abs micro" style="left:0;right:0;top:6px;text-align:center;color:#fff">tamberlybuild.com</div>
    <div class="abs" style="left:0;right:0;top:40px;height:37px;background:var(--paper)"></div>
  </article>
  <div class="label" style="left:364px;top:118px;width:85px">Envelope_Back</div>

  <!-- Folder -->
  <article class="piece folder" style="left:468px;top:18px;width:120px;height:100px;background:none">
    <div class="abs navy" style="left:0;top:0;width:60px;height:100px;padding:4px">
      <div class="micro" style="position:absolute;left:4px;top:62px">5127 Oakmere Lane<br>Ridgeholt, MS 70194<br>(504) 555-0147<br>tamberlybuild.com</div>
      <div class="abs" style="left:0;right:0;bottom:0;height:28px;background:var(--navy-deep)"></div>
    </div>
    <div class="abs" style="left:60px;top:0;width:60px;height:72px;background:var(--paper)">
      <div class="brand abs" style="left:0;right:0;top:28px;text-align:center;font-size:7px">TAMBERLY<small>CONSTRUCTION SERVICES, LLC</small></div>
    </div>
    <div class="abs navy" style="left:60px;top:72px;width:60px;height:28px"></div>
  </article>
  <div class="label" style="left:468px;top:119px;width:120px">Folder</div>

  <!-- Fax sheets -->
  <article class="piece fax" style="left:595px;top:16px;width:79px;height:101px;padding:5px">
    <div class="brand" style="font-size:5px">TAMBERLY<small>CONSTRUCTION SERVICES, LLC</small></div>
    <div class="abs micro" style="left:53px;top:5px">5127 Oakmere Lane<br>Ridgeholt, MS 70194<br>(504) 555-0148</div>
    <div style="display:flex;gap:4px;margin-top:8px">
      <div style="flex:1"><div class="field">To<span></span></div><div class="field">Fax<span></span></div><div class="field">Phone<span></span></div><div class="field">Re<span></span></div></div>
      <div style="flex:1"><div class="field">From<span></span></div><div class="field">Pages<span></span></div><div class="field">Date<span></span></div><div class="field">CC<span></span></div></div>
    </div>
    <div class="micro" style="margin-top:2px">□ Urgent □ For Review □ Please Comment □ Please Reply</div>
    <div class="micro" style="margin-top:3px"><b>Comments:</b></div>
    <div class="abs micro" style="left:0;right:0;bottom:2px;text-align:center;color:var(--muted)">tamberlybuild.com</div>
  </article>
  <div class="label" style="left:595px;top:118px;width:79px">Fax_option_01</div>

  <article class="piece fax" style="left:678px;top:16px;width:79px;height:101px;padding:5px">
    <div class="brand" style="font-size:5px;text-align:center">TAMBERLY<small>CONSTRUCTION SERVICES, LLC</small></div>
    <div style="display:flex;gap:4px;margin-top:8px">
      <div style="flex:1"><div class="field">To<span></span></div><div class="field">Fax<span></span></div><div class="field">Phone<span></span></div><div class="field">Re<span></span></div></div>
      <div style="flex:1"><div class="field">From<span></span></div><div class="field">Pages<span></span></div><div class="field">Date<span></span></div><div class="field">CC<span></span></div></div>
    </div>
    <div class="micro" style="margin-top:2px">□ Urgent □ For Review □ Please Comment □ Please Reply</div>
    <div class="micro" style="margin-top:3px"><b>Comments:</b></div>
    <div class="abs micro" style="left:0;right:0;bottom:2px;text-align:center;color:var(--muted)">5127 Oakmere Lane, Ridgeholt, MS 70194 · tamberlybuild.com</div>
  </article>
  <div class="label" style="left:678px;top:118px;width:79px">Fax_option_02</div>

  <!-- Compliment slip -->
  <article class="piece compliment-slip" style="left:770px;top:27px;width:86px;height:37px">
    <div class="brand abs" style="left:4px;top:5px;font-size:4.5px">TAMBERLY<small>CONSTRUCTION SERVICES, LLC</small></div>
    <div class="abs micro" style="left:62px;top:4px">5127 Oakmere Lane<br>Ridgeholt, MS 70194<br>(504) 555-0147<br>tamberlybuild.com</div>
    <div class="abs script" style="left:22px;top:19px;font-size:8px">With Compliments</div>
  </article>
  <div class="label" style="left:770px;top:65px;width:86px">Compliment Slip</div>

  <!-- Thank you cards -->
  <article class="piece thank-you-front" style="left:764px;top:73px;width:57px;height:37px">
    <div class="brand abs" style="left:0;right:0;top:5px;text-align:center;font-size:4.5px">TAMBERLY<small>CONSTRUCTION SERVICES, LLC</small></div>
    <div class="abs script" style="left:0;right:0;top:18px;text-align:center;font-size:9px">Thank you</div>
  </article>
  <div class="label" style="left:764px;top:111px;width:57px">Thank You Card_Front</div>
  <article class="piece navy thank-you-back" style="left:824px;top:73px;width:57px;height:37px">
    <div class="abs micro" style="left:3px;bottom:3px">5127 Oakmere Lane, Ridgeholt, MS 70194 · (504) 555-0147</div>
  </article>
  <div class="label" style="left:824px;top:111px;width:57px">Thank You Card_Back</div>

  <!-- CD label and cover -->
  <div class="disc navy" style="left:871px;top:6px;width:57px;height:57px">
    <div class="brand" style="font-size:4px;margin-bottom:3px;text-align:center">TAMBERLY</div>
    <div class="hub"></div>
    <div class="micro" style="margin-top:4px">tamberlybuild.com</div>
  </div>
  <div class="label" style="left:871px;top:65px;width:57px">CD</div>
  <article class="piece cd-cover" style="left:934px;top:10px;width:62px;height:50px">
    <div class="abs navy" style="left:0;top:0;width:62px;height:8px"></div>
    <div class="brand abs" style="left:4px;top:14px;font-size:4.5px">TAMBERLY<small>CONSTRUCTION SERVICES, LLC</small></div>
    <div class="abs micro" style="left:4px;bottom:4px">5127 Oakmere Lane, Ridgeholt, MS 70194</div>
  </article>
  <div class="label" style="left:934px;top:62px;width:62px">CD cover</div>

  <!-- Lower row: discs, sleeves, magnets -->
  <div class="disc navy" style="left:683px;top:128px;width:57px;height:57px"><div class="brand" style="font-size:4px;margin-bottom:3px">TAMBERLY</div><div class="hub"></div></div>
  <div class="disc" style="left:749px;top:128px;width:57px;height:57px;background:var(--graphite);color:#fff"><div class="brand on-dark" style="font-size:4px;margin-bottom:3px">TAMBERLY</div><div class="hub"></div></div>
  <div class="disc navy" style="left:683px;top:190px;width:57px;height:57px"><div class="brand" style="font-size:4px;margin-bottom:3px">TAMBERLY</div><div class="hub"></div></div>
  <div class="disc" style="left:749px;top:190px;width:57px;height:57px;background:var(--paper)"><div class="brand" style="font-size:4px;margin-bottom:3px">TAMBERLY</div><div class="hub" style="border-color:#333"></div></div>
  <div class="label" style="left:683px;top:247px;width:123px">CD</div>

  <article class="piece navy cd-sleeve" style="left:820px;top:143px;width:57px;height:40px">
    <div class="brand abs" style="left:3px;top:4px;font-size:4px">TAMBERLY</div>
    <div class="abs micro" style="left:3px;bottom:4px">5127 Oakmere Lane, Ridgeholt, MS 70194</div>
  </article>
  <article class="piece cd-sleeve" style="left:820px;top:196px;width:57px;height:40px">
    <div class="brand abs" style="left:3px;top:4px;font-size:4px">TAMBERLY</div>
    <div class="abs micro" style="left:3px;bottom:4px">5127 Oakmere Lane, Ridgeholt, MS 70194</div>
  </article>

  <div class="disc" style="left:484px;top:222px;width:22px;height:22px;background:var(--paper)"><div class="brand" style="font-size:2.6px">TAMBERLY</div></div>
  <div class="disc navy" style="left:510px;top:222px;width:22px;height:22px"><div class="brand" style="font-size:2.6px">TAMBERLY</div></div>
  <div class="disc" style="left:536px;top:222px;width:22px;height:22px;background:var(--graphite)"><div class="brand on-dark" style="font-size:2.6px">TAMBERLY</div></div>
  <div class="disc" style="left:562px;top:222px;width:22px;height:22px;background:var(--paper);border:1px solid var(--navy)"><div class="brand" style="font-size:2.6px">TAMBERLY</div></div>
  <div class="label" style="left:484px;top:246px;width:100px">Car Magnet</div>

  <!-- Presentation slides -->
  <section class="slide" style="left:1002px;top:13px;text-align:center">
    <div class="brand" style="font-size:8px;margin-top:9px">TAMBERLY<small>CONSTRUCTION SERVICES, LLC</small></div>
    <div style="font-size:4.6px;color:var(--navy);margin-top:10px">Welcome to Our</div>
    <div style="font-size:5.4px;color:var(--navy);font-weight:700">Presentation Name</div>
    <div style="font-size:4px;color:var(--navy)">Description</div>
  </section>

  <section class="slide" style="left:1101px;top:13px">
    <h3>Heading Here</h3><h4>Sub Heading</h4>
    <div style="display:flex;gap:3px">
      <div style="flex:1"><div class="photo">Photo</div><div class="micro"><b>Team member1</b><br>Title<br>Short note on role.</div></div>
      <div style="flex:1"><div class="photo">Photo</div><div class="micro"><b>Team member2</b><br>Title<br>Short note on role.</div></div>
      <div style="flex:1"><div class="photo">Photo</div><div class="micro"><b>Team member3</b><br>Title<br>Short note on role.</div></div>
      <div style="flex:1"><div class="photo">Photo</div><div class="micro"><b>Team member4</b><br>Title<br>Short note on role.</div></div>
    </div>
  </section>

  <section class="slide" style="left:1002px;top:88px">
    <h3>Heading Here</h3><h4>Sub Heading</h4>
    <div style="display:grid;grid-template-columns:1fr 1fr;gap:3px 5px">
      <div class="micro"><b>Group1</b><br>Roof work planned with care and clear cost.</div>
      <div class="micro"><b>Group4</b><br>Gutters fitted to match each home style.</div>
      <div class="micro"><b>Group2</b><br>Patio covers built to last many seasons.</div>
      <div class="micro"><b>Group5</b><br>Siding options chosen with the owner.</div>
      <div class="micro"><b>Group3</b><br>Shutters sized and hung by our crew.</div>
      <div class="micro"><b>Group6</b><br>Waterproofing for decks and floors.</div>
    </div>
  </section>

  <section class="slide" style="left:1101px;top:88px">
    <h3>Heading Here</h3><h4>Sub Heading</h4>
    <svg width="44" height="34" viewBox="0 0 44 34" aria-label="Bar chart">
      <line x1="2" y1="32" x2="42" y2="32" stroke="var(--muted)" stroke-width=".4"/>
      <rect x="4" y="2" width="5" height="30" fill="var(--navy)"/>
      <rect x="11" y="8" width="5" height="24" fill="var(--navy)"/>
      <rect x="18" y="6" width="5" height="26" fill="var(--navy)"/>
      <rect x="25" y="14" width="5" height="18" fill="var(--navy)"/>
      <rect x="32" y="12" width="5" height="20" fill="var(--navy)"/>
    </svg>
    <div class="abs micro" style="left:52px;top:20px;width:31px">Jobs grew each quarter this year across all service lines, led by roofing.</div>
  </section>

  <section class="slide" style="left:1002px;top:163px;height:70px">
    <h3>Heading Here</h3><h4>Sub Heading</h4>
    <p class="micro" style="width:40px">Our team finished more projects this year than ever before. Roofing made up the largest share, with siding and gutters close behind. Customer reviews stayed strong in every area we serve.</p>
    <svg class="abs" style="left:56px;top:22px" width="24" height="24" viewBox="0 0 24 24" aria-label="Pie chart">
      <circle cx="12" cy="12" r="11" fill="var(--navy)"/>
      <path d="M12 12L12 1A11 11 0 0 1 22.5 9Z" fill="#6a6a74"/>
      <path d="M12 12L22.5 9A11 11 0 0 1 19 20.5Z" fill="#b5b5bd"/>
    </svg>
    <div class="abs micro" style="left:56px;top:50px">■ Roofing ■ Siding<br>■ Gutters</div>
  </section>

  <section class="slide navy" style="left:1101px;top:163px;height:70px;background:var(--navy);text-align:center">
    <div style="font-size:14px;margin-top:14px;line-height:1">Thanks</div>
    <div style="font-size:7px">For Coming</div>
    <div class="micro" style="position:absolute;left:0;right:0;bottom:3px">5127 Oakmere Lane, Ridgeholt, MS 70194 · tamberlybuild.com</div>
  </section>
  <div class="label" style="left:1101px;top:240px;width:88px">Power point templete</div>

</main>
</body>
</html>
```